Lumo4Kart - a fintech company - business card

We need a business card design for our Payments Technology company in Sydney, Australia. We provide business with payment solutions expanding across EFTPOS machines, online payment gateways and mobile payment solutions. We would like to see designs that are clean, classy and professional.
Target Market(s)
Business professionals, executives, c-suite
Industry/Entity Type
Fintech
Contact Information for Business Card
Will be on 400gsm. Logo will most likely be spot gloss unless designer recommends otherwise.
Font styles to use
Sans Serif
Requirements
Must have
- We need our website (lumo4kart.com.au), email (contact@lumo4kart.com.au), mobile (0432 587 904) and direct phone number (02 6815 3927) to feature on the card along with our logo (attached) and the words "EFTPOS | ONLINE | MOBILE"
- Font = Roboto

```html
<!DOCTYPE html>
<html lang="en">
<head>
<meta charset="utf-8">
<title>Lumo4Kart business card</title>
<link rel="stylesheet" href="https://fonts.googleapis.com/css2?family=Open+Sans:wght@400;600&family=Roboto:wght@500;700&display=swap">
<style>
  :root {
    --bg: #2a2a2c;
    --card: #1c1d20;
    --card-back: #1a1a1c;
    --pattern: #262629;
    --brand-blue: #14679b;
    --logo-grey: #8a8b8e;
    --silver: #cfcfd1;
    --text-light: #e6e6e8;
    --rule: #55575b;
  }
  * { margin: 0; padding: 0; box-sizing: border-box; }
  html, body { width: 1200px; height: 1108px; overflow: hidden; }
  body {
    background: var(--bg);
    font-family: "Open Sans", Arial, sans-serif;
    display: flex;
    align-items: center;
    justify-content: center;
    gap: 60px;
  }
  .card {
    width: 420px;
    height: 660px;
    border-radius: 26px;
    position: relative;
    overflow: hidden;
    box-shadow: 0 18px 40px rgba(0,0,0,0.45);
  }
  .card-front { background: var(--card); }
  .card-back { background: var(--card-back); }

  .brand {
    position: absolute;
    top: 120px;
    left: 0; right: 0;
    display: flex;
    flex-direction: column;
    align-items: center;
  }
  .brand-mark {
    width: 150px; height: 150px;
    border-radius: 50%;
    background: var(--brand-blue);
  }
  .brand-name {
    margin-top: 18px;
    font-family: "Roboto", Arial, sans-serif;
    font-weight: 700;
    font-size: 52px;
    letter-spacing: 0.5px;
    color: var(--logo-grey);
  }

  .contact {
    position: absolute;
    top: 430px;
    left: 0; right: 0;
    text-align: center;
  }
  .person-name {
    font-family: "Roboto", Arial, sans-serif;
    font-weight: 500;
    font-size: 25px;
    color: var(--brand-blue);
    letter-spacing: 0.3px;
  }
  .person-role {
    font-size: 18px;
    color: var(--text-light);
    margin-top: 2px;
  }
  .rule {
    width: 170px;
    height: 1px;
    background: var(--rule);
    margin: 12px auto 12px;
  }
  .contact-line {
    font-size: 18px;
    line-height: 1.45;
    color: var(--text-light);
  }
  .contact-line .label { color: var(--brand-blue); }
  .contact-web { color: var(--brand-blue); }

  .back-pattern {
    position: absolute;
    top: 0; left: 0; right: 0;
    height: 470px;
    background: linear-gradient(180deg, var(--pattern) 0%, var(--card-back) 100%);
  }
  .back-brand {
    position: absolute;
    left: 0; right: 0;
    bottom: 90px;
    text-align: center;
  }
  .back-name {
    font-family: "Roboto", Arial, sans-serif;
    font-weight: 700;
    font-size: 60px;
    color: var(--silver);
  }
  .tagline {
    margin-top: 6px;
    font-family: "Roboto", Arial, sans-serif;
    font-weight: 500;
    font-size: 19px;
    letter-spacing: 0.5px;
    color: var(--text-light);
  }
</style>
</head>
<body>
  <section class="card card-front">
    <div class="brand">
      <div class="brand-mark"></div>
      <div class="brand-name">LUMO4KART</div>
    </div>
    <div class="contact">
      <div class="person-name">DANIEL HARTLEY</div>
      <div class="person-role">Managing Director</div>
      <div class="rule"></div>
      <div class="contact-line"><span class="label">M:</span> 0432 587 904</div>
      <div class="contact-line"><span class="label">P:</span> 02 6815 3927</div>
      <div class="contact-line"><span class="label">E:</span> contact@lumo4kart.com.au</div>
      <div class="contact-line contact-web">www.lumo4kart.com.au</div>
    </div>
  </section>

  <section class="card card-back">
    <div class="back-pattern" role="img" aria-label="Faint repeating brand symbol pattern"></div>
    <div class="back-brand">
      <div class="back-name">LUMO4KART</div>
      <div class="tagline">EFTPOS | ONLINE | MOBILE</div>
    </div>
  </section>
</body>
</html>
```